Business card

would like a double sided business card made up with my logos provided.
Prefer card to have black background and to use the black logos, with matching blue writing for the text.
One side to just be the logo, (Try to use both the black logos)
the other side to have the logo and also my credentials/business information.

Covering all aspects of Carpentry and Building Services

Marcus Tolvey
Qualified Carpenter
Mob: 0417263948
Email: rkt.joinery@mailbright.com
ABN: 47 615 209 834

Industry/Entity Type

Business

Contact Information for Business Card

Marcus Tolvey
Qualified Carpenter
Mob: 0417263948
ABN: 47 615 209 834

Requirements
Must have
• Please try to use both the black logos and incorporate into the card.

```html
<!DOCTYPE html>
<html lang="en">
<head>
<meta charset="utf-8">
<title>RKT Joinery – Business Card</title>
<link rel="stylesheet" href="https://fonts.googleapis.com/css2?family=PT+Sans:wght@400;700&family=Roboto:wght@400&display=swap">
<style>
  :root {
    --stage: #9a9a9a;
    --card-light: #ffffff;
    --card-dark: #272727;
    --ink-dark: #2b2b2b;
    --ink-grey: #878787;
    --ink-soft: #e2e2e2;
    --brand-blue: #1a84cc;
    --badge-frame: #050505;
    --badge-fill: #232323;
  }
  * { margin: 0; padding: 0; box-sizing: border-box; }
  html, body {
    width: 1130px; height: 1200px; overflow: hidden;
    background: var(--stage);
  }
  .stage { position: relative; width: 1130px; height: 1200px; }
  .card {
    position: absolute; left: 164px; width: 806px; height: 461px;
  }
  .card--front { top: 99px; background: var(--card-light); }
  .card--back { top: 639px; background: var(--card-dark); }
  .card > * { position: absolute; line-height: 1; white-space: nowrap; }

  .brand-name {
    font-family: "PT Sans", sans-serif; font-weight: 700;
    letter-spacing: 1px;
  }
  .card--front .brand-name {
    left: 152px; top: 50px; font-size: 64px; color: var(--ink-dark);
  }
  .person-name {
    font-family: "PT Sans", sans-serif; font-weight: 700;
  }
  .card--front .person-name {
    left: 152px; top: 172px; font-size: 55px; color: var(--ink-grey);
  }
  .role {
    font-family: "PT Sans", sans-serif; color: var(--brand-blue);
  }
  .card--front .role { left: 184px; top: 229px; font-size: 34px; }
  .contact-list { left: 152px; top: 295px; list-style: none; }
  .contact-list li {
    font-family: "Roboto", sans-serif; font-size: 21px;
    color: var(--ink-grey); height: 40.5px;
  }

  .card--back .person-name {
    left: 199px; top: 77px; font-size: 56px; color: var(--ink-soft);
  }
  .card--back .role {
    left: 375px; top: 148px; font-size: 16px; font-weight: 700;
    letter-spacing: .3px;
  }
  .brand-badge {
    left: 184px; top: 201px; width: 389px; height: 112px;
    background: var(--badge-fill); border: 7px solid var(--badge-frame);
    border-radius: 10px;
    display: flex; align-items: center; justify-content: center;
  }
  .brand-badge .brand-name { position: static; font-size: 46px; color: #ffffff; }
  .tagline {
    left: 0; width: 100%; text-align: center; top: 343px;
    font-family: "PT Sans", sans-serif; font-size: 24px; color: var(--brand-blue);
  }
</style>
</head>
<body>
<main class="stage">
  <section class="card card--front" aria-label="Card front">
    <div class="brand-name">RKT JOINERY</div>
    <h1 class="person-name">Marcus Tolvey</h1>
    <p class="role">Qualified Carpenter</p>
    <ul class="contact-list">
      <li>Email: rkt.joinery@mailbright.com</li>
      <li>ABN: 47 615 209 834</li>
      <li>Mobile: 0417263948</li>
    </ul>
  </section>
  <section class="card card--back" aria-label="Card back">
    <h2 class="person-name">Marcus Tolvey</h2>
    <p class="role">QUALIFIED CARPENTER</p>
    <div class="brand-badge"><span class="brand-name">RKT JOINERY</span></div>
    <p class="tagline">Covering all aspects of Carpentry and Building Services</p>
  </section>
</main>
</body>
</html>
```